Business Card Design

I am a voice actor and need a business card to match the design of my website, www.tamsinharlowe.com. The colors are red, black and white. I've attached a pic of the back of a business card I thought was cool that for my design, could maybe have the black and white background from my website and the website address going across the middle of the card in red...or within a red square and white lettering..?? Just play around with it. Also wanting to keep the fonts on the business card similar to those on the website. I also attached a copy of the front of a business card that I liked. My design does not have to look like this.
I have a tag line, but not sure it will be too much to add to my business card or not. Would like to see the design with the tag and without it. "Spoken with Care..." you'll see it on my website.
I will be ordering additional items from the chosen designer. I need a nice logo to use on my invoices, notecards and I need a letterhead design. Thank you so much for being artistically brilliant!
Industry/Entity Type
Business
Contact Information for Business Card
Tamsin Harlowe
Voice Actor
Email: Tamsin@TamsinHarlowe.com
Website: www.TamsinHarlowe.com

```html
<!DOCTYPE html>
<html lang="en">
<head>
<meta charset="utf-8">
<title>Tamsin Harlowe – Business Card</title>
<link href="https://fonts.googleapis.com/css2?family=Playfair+Display:wght@400;700&display=swap" rel="stylesheet">
<style>
  :root {
    --backdrop: #2b2b2c;
    --card-black: #1d1e20;
    --gloss-dark: #111213;
    --gloss-light: #5a5b5e;
    --accent-red: #a3262a;
    --edge-red: #6e1518;
    --ink-white: #f2f2f2;
  }
  html, body {
    margin: 0;
    width: 1200px;
    height: 900px;
    overflow: hidden;
    background: var(--backdrop);
  }
  .canvas {
    position: relative;
    width: 1200px;
    height: 900px;
  }
  .card {
    position: absolute;
    width: 560px;
    height: 320px;
    background: var(--card-black);
    box-sizing: border-box;
    box-shadow: 0 12px 30px rgba(0,0,0,0.45);
  }
  /* Front: name and contact */
  .card-front {
    left: 70px;
    top: 110px;
    padding: 48px 56px;
  }
  .identity {
    display: inline-block;
  }
  .name {
    margin: 0;
    font-family: "Playfair Display", serif;
    font-weight: 400;
    font-size: 46px;
    line-height: 1;
    color: var(--accent-red);
    letter-spacing: 0.02em;
  }
  .role {
    margin: 6px 0 0;
    font-family: "Playfair Display", serif;
    font-size: 15px;
    letter-spacing: 0.55em;
    color: var(--accent-red);
    text-transform: uppercase;
  }
  .tagline {
    margin: 4px 0 0;
    text-align: right;
    font-family: "Playfair Display", serif;
    font-weight: 400;
    font-size: 18px;
    color: var(--accent-red);
  }
  .contact {
    list-style: none;
    margin: 36px 0 0;
    padding: 0;
    font-family: "Playfair Display", serif;
    font-size: 15px;
    line-height: 1.7;
    color: var(--ink-white);
  }
  .contact-label {
    color: var(--accent-red);
    margin-right: 6px;
  }
  /* Back: pattern and web address */
  .card-back {
    left: 570px;
    top: 470px;
    border-bottom: 5px solid var(--edge-red);
    overflow: hidden;
    display: flex;
    align-items: center;
    justify-content: center;
  }
  .vine-pattern {
    position: absolute;
    inset: 0;
    background:
      radial-gradient(ellipse at 25% 45%, var(--gloss-dark) 0%, transparent 55%),
      radial-gradient(ellipse at 85% 70%, var(--gloss-light) 0%, transparent 55%),
      var(--card-black);
  }
  .web-address {
    position: relative;
    margin: 0;
    font-family: "Playfair Display", serif;
    font-weight: 700;
    font-size: 36px;
    color: var(--accent-red);
    letter-spacing: 0.01em;
  }
</style>
</head>
<body>
<main class="canvas">
  <section class="card card-front" aria-label="Business card front">
    <div class="identity">
      <h1 class="name">Tamsin Harlowe</h1>
      <p class="role">Voice Actor</p>
      <p class="tagline">Spoken with Care</p>
    </div>
    <ul class="contact">
      <li><span class="contact-label">E.</span>Tamsin@TamsinHarlowe.com</li>
      <li><span class="contact-label">W.</span>www.TamsinHarlowe.com</li>
    </ul>
  </section>

  <section class="card card-back" aria-label="Business card back">
    <div class="vine-pattern" role="img" aria-label="Glossy black and grey pattern of curling vines and leaves"></div>
    <p class="web-address">www.TamsinHarlowe.com</p>
  </section>
</main>
</body>
</html>
```